I am looking for business cards and letterhead

I want a high-level look for CEO's who want a concierge level leadership consultant and organization development strategist

This needs to go with my brand: simple, elegant, clean. Please improve on this design while using these fonts and colors

Here is my website: CorinneHalvers.com

```html
<!DOCTYPE html>
<html lang="en">
<head>
<meta charset="utf-8">
<title>Corinne Halvers — Business Cards &amp; Letterhead</title>
<link rel="stylesheet" href="https://fonts.googleapis.com/css2?family=Montserrat:wght@400;500;600;700&family=Raleway:wght@400;500&display=swap">
<style>
  :root {
    --canvas: #e3e3e3;
    --paper: #f6f6f5;
    --navy-deep: #081446;
    --navy: #122a7a;
    --teal: #1b5d7b;
    --gold: #b4975f;
    --ink: #222427;
    --muted: #7b7d80;
    --rule: #c9c9c9;
  }
  * { box-sizing: border-box; margin: 0; padding: 0; }
  html, body { width: 1200px; height: 770px; overflow: hidden; }
  body { background: var(--canvas); font-family: "Montserrat", sans-serif; color: var(--ink); position: relative; }

  /* Business card – front */
  .card { position: absolute; left: 34px; width: 492px; height: 280px; overflow: hidden; }
  .card-front {
    top: 97px;
    background: radial-gradient(ellipse at 50% 40%, var(--navy) 0%, var(--navy-deep) 75%);
  }
  .front-mark {
    position: absolute; left: 165px; top: 41px; width: 162px; height: 162px;
    border: 2px solid rgba(60, 90, 190, .45); border-radius: 50%;
    display: flex; align-items: center; justify-content: center;
  }
  .front-mark span { font-size: 15px; font-weight: 600; color: rgba(90, 120, 210, .7); letter-spacing: .5px; }
  .front-web {
    position: absolute; left: 0; right: 0; top: 233px; text-align: center;
    font-size: 13px; font-weight: 500; letter-spacing: 1.2px; color: #fff;
  }
  .front-web .accent { color: var(--gold); }

  /* Business card – back */
  .card-back { top: 401px; background: var(--paper); }
  .back-mark {
    position: absolute; left: 84px; top: 53px; width: 112px; height: 112px;
    border: 2px solid var(--gold); border-radius: 50%;
    display: flex; align-items: center; justify-content: center; text-align: center;
  }
  .back-mark span { font-size: 12px; font-weight: 600; color: var(--teal); line-height: 1.3; }
  .back-divider { position: absolute; left: 217px; top: 37px; width: 1px; height: 144px; background: var(--rule); }
  .back-details { position: absolute; left: 242px; top: 34px; }
  .person-name { font-size: 23px; font-weight: 600; color: var(--teal); letter-spacing: -.2px; }
  .person-role { font-size: 13px; font-weight: 500; color: var(--muted); margin-top: 1px; }
  .person-address { font-size: 14px; line-height: 17px; margin-top: 11px; color: var(--ink); }
  .contact-line { display: flex; align-items: center; gap: 8px; font-size: 15px; margin-top: 4px; }
  .contact-line svg { flex: none; }
  .contact-line.email { font-size: 13.5px; margin-top: 3px; }
  .tagline {
    position: absolute; left: 0; right: 0; top: 226px; text-align: center;
    font-size: 13.5px; font-weight: 600; color: #3a3b3d;
  }
  .card-band { position: absolute; left: 0; bottom: 0; width: 492px; height: 28px; }
  .band-web {
    position: absolute; right: 12px; bottom: 6px; display: flex; align-items: center; gap: 6px;
    font-size: 13.5px; font-weight: 500; color: #fff; letter-spacing: .3px;
  }

  /* Letterhead */
  .letterhead { position: absolute; left: 652px; top: 34px; width: 497px; height: 702px; background: var(--paper); overflow: hidden; }
  .lh-mark {
    position: absolute; left: 44px; top: 34px; width: 72px; height: 72px;
    border: 1.5px solid var(--gold); border-radius: 50%;
    display: flex; align-items: center; justify-content: center; text-align: center;
  }
  .lh-mark span { font-size: 8px; font-weight: 600; color: var(--teal); line-height: 1.3; }
  .lh-contact { position: absolute; left: 344px; top: 44px; border-left: 1px solid var(--rule); padding-left: 14px; font-size: 7.6px; line-height: 11px; }
  .lh-contact .row { display: flex; align-items: center; gap: 4px; }
  .lh-contact .phone { margin-top: 3px; }
  .lh-heading { position: absolute; left: 43px; right: 44px; top: 180px; display: flex; justify-content: space-between; font-size: 11px; font-family: "Raleway", sans-serif; font-weight: 500; }
  .lh-heading .date { color: #555; }
  .lh-body { position: absolute; left: 43px; width: 410px; top: 226px; font-family: "Raleway", sans-serif; font-size: 7.4px; line-height: 10px; text-align: justify; color: #333; }
  .lh-body p + p { margin-top: 12px; }
  .lh-closing { position: absolute; left: 43px; top: 536px; font-family: "Raleway", sans-serif; }
  .lh-closing .sign-off { font-size: 7.4px; color: #333; }
  .lh-closing .signer { font-size: 11px; margin-top: 8px; }
  .signature { position: absolute; left: 41px; top: 571px; width: 123px; height: 34px; background: linear-gradient(90deg, #e6e6e6, #efefef); border-radius: 3px; }
  .lh-band { position: absolute; left: 0; bottom: 0; width: 497px; height: 20px; }
  .lh-web { position: absolute; right: 44px; bottom: 5px; font-size: 6.8px; color: #fff; letter-spacing: .2px; }
</style>
</head>
<body>

  <section class="card card-front" aria-label="Business card front">
    <div class="front-mark"><span>Corinne Halvers</span></div>
    <p class="front-web">www.<span class="accent">corinnehalvers</span>.com</p>
  </section>

  <section class="card card-back" aria-label="Business card back">
    <div class="back-mark"><span>Corinne<br>Halvers</span></div>
    <div class="back-divider"></div>
    <div class="back-details">
      <h1 class="person-name">Corinne Halvers</h1>
      <p class="person-role">Founder &amp; CEO</p>
      <p class="person-address">4470 Harbor View Pkwy<br>210-B, FL 32541</p>
      <p class="contact-line">
        <svg width="13" height="13" viewBox="0 0 24 24" aria-hidden="true"><path fill="#b4975f" d="M6.6 10.8a15.1 15.1 0 0 0 6.6 6.6l2.2-2.2c.3-.3.7-.4 1-.2 1.1.4 2.3.6 3.6.6.6 0 1 .4 1 1V20c0 .6-.4 1-1 1A17 17 0 0 1 3 4c0-.6.4-1 1-1h3.5c.6 0 1 .4 1 1 0 1.3.2 2.5.6 3.6.1.3 0 .7-.2 1z"/></svg>
        044-555 010 202
      </p>
      <p class="contact-line email">
        <svg width="13" height="13" viewBox="0 0 24 24" aria-hidden="true"><path fill="#b4975f" d="M2 11 22 3l-6 18-4-7z"/></svg>
        hello@corinnehalvers.com
      </p>
    </div>
    <p class="tagline">Elite Leadership Transformation &amp; Organization Development</p>
    <svg class="card-band" viewBox="0 0 492 28" preserveAspectRatio="none" aria-hidden="true">
      <polygon points="0,0 284,0 276,8 0,8" fill="#b4975f"/>
      <polygon points="290,0 492,0 492,28 0,28 0,14 280,14" fill="#1b5d7b"/>
    </svg>
    <p class="band-web">
      <svg width="13" height="13" viewBox="0 0 24 24" aria-hidden="true"><g fill="none" stroke="#fff" stroke-width="2"><circle cx="12" cy="12" r="9"/><path d="M3 12h18M12 3c3 3 3 15 0 18M12 3c-3 3-3 15 0 18"/></g></svg>
      www.corinnehalvers.com
    </p>
  </section>

  <section class="letterhead" aria-label="Letterhead">
    <div class="lh-mark"><span>Corinne<br>Halvers</span></div>
    <div class="lh-contact">
      <p>4470 Harbor View Pkwy<br>210-B, FL 32541</p>
      <p class="row phone"><svg width="7" height="7" viewBox="0 0 24 24" aria-hidden="true"><path fill="#1b5d7b" d="M6.6 10.8a15.1 15.1 0 0 0 6.6 6.6l2.2-2.2c.3-.3.7-.4 1-.2 1.1.4 2.3.6 3.6.6.6 0 1 .4 1 1V20c0 .6-.4 1-1 1A17 17 0 0 1 3 4c0-.6.4-1 1-1h3.5c.6 0 1 .4 1 1 0 1.3.2 2.5.6 3.6.1.3 0 .7-.2 1z"/></svg>044-555 010 202</p>
      <p class="row"><svg width="7" height="7" viewBox="0 0 24 24" aria-hidden="true"><path fill="#1b5d7b" d="M2 11 22 3l-6 18-4-7z"/></svg>hello@corinnehalvers.com</p>
    </div>

    <div class="lh-heading"><span>Dear, Corinne Halvers</span><span class="date">Date: 24 Oct’ 2025</span></div>

    <div class="lh-body">
      <p>Thank you for the thoughtful conversation last week about the next chapter of your leadership team. As promised, this letter outlines how a concierge advisory engagement would support you, your executives and the wider organization over the coming year. Our work begins with listening: private interviews, a review of your strategy, and time spent observing how decisions are made across the business.</p>
      <p>From there we shape a tailored plan. Each executive receives one-to-one coaching focused on clarity, presence and accountability, while the team as a whole works through a series of structured sessions on alignment and trust. You will have direct access to me between meetings, so that questions can be answered while they still matter and momentum is never lost.</p>
      <p>Alongside the coaching, we will look closely at the structure of the organization itself. Roles, reporting lines and meeting rhythms often grow by accident rather than design, and small changes here can free a great deal of energy. I will bring you clear recommendations, a realistic timeline and simple measures so that progress can be seen by everyone, not only by the leadership team. Every step is agreed with you in advance.</p>
      <p>I have enclosed a short proposal with fees and scheduling options for your review. I would welcome the chance to discuss it at a time that suits you, and I look forward to working together.</p>
    </div>

    <div class="lh-closing">
      <p class="sign-off">Yours Sincerely</p>
      <p class="signer">Corinne Halvers</p>
    </div>
    <div class="signature" role="img" aria-label="Handwritten signature of Corinne Halvers"></div>

    <svg class="lh-band" viewBox="0 0 497 20" preserveAspectRatio="none" aria-hidden="true">
      <polygon points="0,0 358,0 353,6 0,6" fill="#b4975f"/>
      <polygon points="362,0 497,0 497,20 0,20 0,10 354,10" fill="#1b5d7b"/>
    </svg>
    <p class="lh-web">www.corinnehalvers.com</p>
  </section>

</body>
</html>
```